Flyer Pacific Beach Marijuana Delivery Service Flyer

double sided color flyer

Flyer dimensions: 5.5"x4.5"

BACKSIDE:
Insert: ​KNOW THE DIFFERECE
(Please enhance this image make more vibrant, fun, eye catchy)

FRONTSIDE:
-White Background Insert Outline of Green Jar from images to Fill White Space

-All Text/content to appear INSIDE the green outline drawing of jar

-Keep Layout/ fonts, text size similar to uploaded image

-The front of my flyer should look like the uploaded image of jar

FREE & FAST (large bold font)

DELIVERY (appears on arching banner)

707-286-1947 (BOLD)
TEXT TO ORDER NOW!
TODAY'S SPECIALS TEXT: MENU (reverse highlight this text)

12PM-10PM.7DAYS (arch text like uploaded image)

ESTD (insert pot leaf image) 2018

ALL FIRST TIME PATIENTS RECIEVE 1 FREE GRAM

K.T. HAZE HOUR:
4grms - $45
8grms - $80
1oz - $260
(please be creative with this text, use bubbles/banners/badges to make K.T. HAZE HOUR pop and stand out)

21+ ID REQUIRED

MARIJUANA DELIVERY

```html
<!DOCTYPE html>
<html lang="en">
<head>
<meta charset="utf-8">
<title>Harbor Leaf Delivery Flyers</title>
<link rel="stylesheet" href="https://fonts.googleapis.com/css2?family=Bangers&family=Black+Ops+One&family=Kaushan+Script&family=Open+Sans:wght@400;600;700;800&family=Oswald:wght@400;500;600;700&display=swap">
<style>
:root{
  --stage:#6f6f74;
  --green:#2f9a3a;
  --green-dark:#1f7a2b;
  --lime:#8fd32a;
  --ink:#1d1d1d;
  --concrete:#e6e6e2;
  --white:#ffffff;
  --parchment:#d9c49a;
  --parchment-edge:#a88a57;
  --orange:#f07a22;
  --sunset-top:#2a2a30;
}
*{box-sizing:border-box;margin:0;padding:0}
html,body{width:1200px;height:1200px;overflow:hidden}
body{background:var(--stage);font-family:"Open Sans",sans-serif;position:relative}

.flyer{position:absolute;overflow:hidden}

/* front */
.flyer-front{left:41px;top:133px;width:545px;height:665px;background:var(--concrete)}
.leaf-decor{position:absolute}
.leaf-tl{left:0;top:0;width:120px;height:110px;background:radial-gradient(circle at 30% 30%,#7bc043 0,#7bc04300 70%)}
.leaf-tr{right:0;top:0;width:150px;height:150px;background:radial-gradient(circle at 75% 25%,#7bc043 0,#7bc04300 70%)}
.plant-photo{left:0;top:460px;width:200px;height:205px;background:radial-gradient(circle at 30% 50%,#6fae2e 0,#9ac95a 45%,#e6e6e200 75%)}
.brand-tab{position:absolute;left:177px;top:0;width:185px;height:41px;background:var(--ink);border:3px solid var(--green);border-top:0;border-radius:0 0 12px 12px;display:flex;align-items:center;justify-content:center;font-family:"Oswald",sans-serif;font-weight:600;font-size:21px;line-height:1;color:var(--lime);letter-spacing:1px}
.jar{position:absolute;left:123px;top:63px;width:305px;height:589px;background:var(--white);border:5px solid var(--green);border-radius:40px 40px 34px 34px;box-shadow:0 0 0 2px #fff,0 0 0 5px var(--green)}
.jar-content{position:absolute;inset:0;text-align:center;color:var(--green)}
.jar-content > *{position:absolute;line-height:1}
.headline{left:0;width:100%;top:10px;font-family:"Oswald",sans-serif;font-weight:400;font-size:42px;letter-spacing:2px;color:#dfeee0;-webkit-text-stroke:1.6px #4b5b4c}
.ribbon{left:-24px;top:56px;width:343px;height:56px}
.truck{left:130px;top:104px;width:42px;height:28px}
.phone{left:0;width:100%;top:138px;font-family:"Oswald",sans-serif;font-weight:700;font-size:32px;color:var(--green-dark);letter-spacing:1px}
.order-bar{left:14px;width:267px;top:178px;height:26px;background:var(--green);color:#fff;font-family:"Oswald",sans-serif;font-weight:500;font-size:19px;line-height:26px;letter-spacing:.5px}
.specials{left:0;width:100%;top:216px;font-family:"Oswald",sans-serif;font-weight:600;font-size:18px;color:var(--green-dark)}
.menu{left:0;width:100%;top:239px;font-family:"Oswald",sans-serif;font-weight:500;font-size:30px;color:#4c8a4f;letter-spacing:2px}
.hours{left:-8px;top:270px;width:311px;height:60px}
.est{left:0;width:100%;top:322px;font-family:"Oswald",sans-serif;font-weight:600;font-size:22px;color:var(--green-dark);display:flex;justify-content:center;align-items:center;gap:6px}
.est .stars{font-size:13px;color:var(--green)}
.est .leaf-dot{width:26px;height:18px;border-radius:50%;background:#6fae2e}
.first-time{left:14px;width:267px;top:352px;height:18px;background:var(--green);color:#fff;font-family:"Oswald",sans-serif;font-weight:700;font-size:16px;line-height:18px}
.patients{left:0;width:100%;top:374px;font-family:"Oswald",sans-serif;font-weight:700;font-size:17px;color:var(--green-dark)}
.free-gram{left:6px;top:402px;width:200px;font-family:"Kaushan Script",cursive;font-size:32px;color:var(--green);transform:rotate(-5deg);white-space:nowrap}
.deals-title{left:11px;top:456px;font-family:"Oswald",sans-serif;font-weight:700;font-size:20px;color:var(--green);letter-spacing:.5px}
.prices{left:36px;top:484px;display:flex;gap:9px}
.price{width:48px;height:48px;border-radius:50%;background:var(--green-dark);border:3px solid #fff;box-shadow:0 0 0 2px var(--green-dark);color:#fff;display:flex;flex-direction:column;align-items:center;justify-content:center;line-height:1}
.price b{font-family:"Oswald",sans-serif;font-size:16px;font-weight:700}
.price small{font-size:8px;margin-top:2px}
.id-band{left:0;right:0;bottom:0;height:30px;background:var(--green);border-radius:0 0 28px 28px;color:#fff;font-size:13px;font-weight:600;line-height:28px !important;text-align:center}
.mascot{position:absolute;border-radius:12px}
.mascot-front{left:380px;top:490px;width:165px;height:175px;background:radial-gradient(circle at 55% 60%,#4cae2e 0,#8fd32a 45%,#e6e6e200 72%)}
.bubble{position:absolute;background:#fff;border:2px solid var(--ink);border-radius:50%;font-family:"Oswald",sans-serif;font-weight:600;line-height:1;color:var(--green);display:flex;align-items:center;justify-content:center;transform:rotate(-14deg)}
.bubble-front{left:368px;top:470px;width:98px;height:54px;font-size:16px}

/* back */
.flyer-back{left:611px;top:371px;width:549px;height:669px;background:var(--orange)}
.sunset-photo{position:absolute;left:0;top:0;width:100%;height:440px;background:linear-gradient(180deg,var(--sunset-top) 0,#7a3a1e 14%,#e8742a 26%,#b0542a 38%,#3a2a2a 62%,#5a2d1e 80%,#f07a2200 100%)}
.knowline{position:absolute;right:12px;top:10px;font-family:"Bangers",cursive;font-size:36px;line-height:1;letter-spacing:1px;color:#fff}
.knowline span{color:var(--lime)}
.parchment{position:absolute;left:27px;top:150px;width:485px;height:482px;background:radial-gradient(ellipse at 50% 45%,#e6d3a8 0,var(--parchment) 55%,var(--parchment-edge) 100%);transform:rotate(-3deg);box-shadow:2px 4px 10px rgba(0,0,0,.5)}
.parchment-frame{position:absolute;inset:14px;border:2px solid #3a2e1e}
.cmd-title{position:absolute;left:0;width:100%;top:36px;text-align:center;font-family:"Black Ops One",sans-serif;line-height:1}
.cmd-title .t1{display:block;font-size:36px;color:var(--green)}
.cmd-title .t2{display:block;font-size:40px;color:var(--ink);margin-top:4px}
.cmd-list{position:absolute;left:30px;top:136px;width:420px;list-style:none;font-size:14.5px;line-height:19px;color:#1f1a12}
.cmd-list li{padding-left:16px;text-indent:-16px}
.cmd-list li.narrow{max-width:240px}
.cmd-list b{font-weight:700}
.cmd-phone{display:inline-block;font-family:"Oswald",sans-serif;font-weight:600;font-size:24px;line-height:28px;color:#fff;-webkit-text-stroke:1px #3a2e1e;text-indent:0}
.side-tab{position:absolute;left:0;top:480px;width:34px;height:189px;background:var(--green);border-radius:0 12px 0 0;display:flex;align-items:center;justify-content:center}
.side-tab span{transform:rotate(-90deg);white-space:nowrap;font-family:"Oswald",sans-serif;font-weight:600;font-size:18px;color:#fff;letter-spacing:1px}
.mascot-back{left:345px;top:480px;width:200px;height:189px;background:radial-gradient(circle at 55% 60%,#4cae2e 0,#8fd32a 45%,#f07a2200 72%)}
.bubble-back{left:325px;top:462px;width:112px;height:60px;font-size:17px}
</style>
</head>
<body>

<section class="flyer flyer-front" aria-label="Front of delivery flyer">
  <div class="leaf-decor leaf-tl" role="img" aria-label="Cannabis leaf decoration"></div>
  <div class="leaf-decor leaf-tr" role="img" aria-label="Cannabis leaf decoration"></div>
  <div class="leaf-decor plant-photo" role="img" aria-label="Photo of a cannabis plant"></div>

  <div class="brand-tab">HARBOR LEAF</div>

  <div class="jar">
    <div class="jar-content">
      <div class="headline">FREE &amp; FAST</div>
      <svg class="ribbon" viewBox="0 0 343 56">
        <path d="M0 24 L28 20 L22 38 L32 54 L0 50 Z" fill="#1f7a2b"/>
        <path d="M343 24 L315 20 L321 38 L311 54 L343 50 Z" fill="#1f7a2b"/>
        <path d="M22 12 Q171 -6 321 12 L321 44 Q171 26 22 44 Z" fill="#2f9a3a"/>
        <path id="ribbonArc" d="M40 34 Q171 16 303 34" fill="none"/>
        <text font-family="Oswald, sans-serif" font-size="21" font-weight="500" fill="#fff" letter-spacing="5" text-anchor="middle"><textPath href="#ribbonArc" startOffset="50%">DELIVERY</textPath></text>
      </svg>
      <svg class="truck" viewBox="0 0 42 28">
        <rect x="8" y="4" width="20" height="16" fill="#1f7a2b"/>
        <path d="M28 9 H35 L40 15 V20 H28 Z" fill="#1f7a2b"/>
        <circle cx="14" cy="22" r="4" fill="#1f7a2b" stroke="#fff" stroke-width="1.5"/>
        <circle cx="34" cy="22" r="4" fill="#1f7a2b" stroke="#fff" stroke-width="1.5"/>
        <rect x="0" y="7" width="6" height="2" fill="#1f7a2b"/>
        <rect x="2" y="12" width="5" height="2" fill="#1f7a2b"/>
      </svg>
      <div class="phone">707-286-1947</div>
      <div class="order-bar">TEXT TO ORDER NOW!</div>
      <div class="specials">TODAY'S SPECIALS TEXT:</div>
      <div class="menu">MENU</div>
      <svg class="hours" viewBox="0 0 311 60">
        <path id="hoursArc" d="M10 54 Q155 14 301 54" fill="none"/>
        <text font-family="Oswald, sans-serif" font-size="34" font-weight="500" fill="#d6ecd6" stroke="#2f9a3a" stroke-width="1.2" text-anchor="middle"><textPath href="#hoursArc" startOffset="50%">12PM-10PM.7DAYS</textPath></text>
      </svg>
      <div class="est"><span class="stars">★★★</span>EST<span class="leaf-dot" role="img" aria-label="Pot leaf"></span>2018<span class="stars">★★★</span></div>
      <div class="first-time">ALL FIRST TIME</div>
      <div class="patients">PATIENTS RECEIVE</div>
      <div class="free-gram">1 FREE Gram</div>
      <div class="deals-title">K.T. HAZE HOUR</div>
      <div class="prices">
        <div class="price"><b>$45</b><small>4 Gr</small></div>
        <div class="price"><b>$80</b><small>8 Gr</small></div>
        <div class="price"><b>$260</b><small>1 Oz</small></div>
      </div>
      <div class="id-band">21+ ID REQUIRED</div>
    </div>
  </div>

  <div class="mascot mascot-front" role="img" aria-label="Cartoon leaf mascot giving an OK sign"></div>
  <div class="bubble bubble-front">707 286 1947</div>
</section>

<section class="flyer flyer-back" aria-label="Back of delivery flyer">
  <div class="sunset-photo" role="img" aria-label="Photo of surfers at a pier at sunset"></div>
  <div class="knowline"><span>KNOW</span> THE DIFFERENCE!</div>

  <div class="parchment">
    <div class="parchment-frame"></div>
    <h2 class="cmd-title"><span class="t1">THE STONER</span><span class="t2">COMMANDMENTS</span></h2>
    <ol class="cmd-list">
      <li><b>I.</b> Mary Jane is thy God, thou shalt not smoke to any other Gods besides she.</li>
      <li><b>II.</b> They who roll, shall light the first spark.</li>
      <li><b>III.</b> Thou shalt not let thy ganja be burned in vain.</li>
      <li><b>IV.</b> Remember to keep holy the hour of 4:20.</li>
      <li><b>V.</b> Thou shalt not mooch off the herb of others.</li>
      <li><b>VI.</b> Thou shalt not bogart.</li>
      <li class="narrow"><b>VII.</b> Thou shalt always puff, puff, pass, and to thy left.</li>
      <li class="narrow"><b>VIII.</b> Thou shalt not steal thy neighbor's lighter.</li>
      <li class="narrow"><b>IX.</b> Thou shalt always be chill with thy buds.</li>
      <li class="narrow"><b>X.</b> Thou shalt not covet thy friend's smoking piece.</li>
      <li class="narrow"><b>XI. Text Your Order to</b><br><span class="cmd-phone">707 286 1947</span></li>
    </ol>
  </div>

  <div class="side-tab"><span>HARBOR LEAF</span></div>
  <div class="mascot mascot-back" role="img" aria-label="Cartoon leaf mascot giving an OK sign"></div>
  <div class="bubble bubble-back">707 286 1947</div>
</section>

</body>
</html>
```